New signage for workshop frontage. Corvane Industrial Repair & Tooling is the company name. Looking for a cool font, metal fabrication is the trade. Also use CIRT as the logo

```html
<!DOCTYPE html>
<html lang="en">
<head>
<meta charset="utf-8">
<title>Corvane Industrial Repair &amp; Tooling – Workshop Sign</title>
<link rel="stylesheet" href="https://fonts.googleapis.com/css2?family=Black+Ops+One&family=Bebas+Neue&family=Poppins:wght@400;600&display=swap">
<style>
  :root {
    --page: #ffffff;
    --sign: #ffffff;
    --steel-dark: #3c3d3f;
    --steel-mid: #6a6b6e;
    --band: #4a4b4e;
    --band-deep: #3f4043;
    --brand-blue: #1a7cc7;
    --ink: #2f3032;
    --text-light: #f4f4f4;
    --text-soft: #d9d9db;
  }
  html, body {
    margin: 0;
    padding: 0;
    width: 837px;
    height: 1200px;
    overflow: hidden;
    background: var(--page);
  }
  .canvas {
    position: relative;
    width: 837px;
    height: 1200px;
  }
  .sign {
    position: absolute;
    left: 30px;
    top: 325px;
    width: 777px;
    height: 549px;
    background: var(--sign);
    box-shadow: 0 2px 10px rgba(0, 0, 0, 0.28);
  }
  .sign svg {
    display: block;
    width: 777px;
    height: 549px;
  }
  .headline {
    font-family: "Black Ops One", "Impact", sans-serif;
  }
  .tab-label {
    font-family: "Poppins", "Arial", sans-serif;
    font-weight: 600;
    fill: var(--text-light);
  }
  .service {
    font-family: "Bebas Neue", "Oswald", sans-serif;
    fill: var(--text-light);
  }
  .service-divider {
    stroke: var(--text-soft);
    stroke-width: 1.2;
  }
  .tagline {
    font-family: "Poppins", "Arial", sans-serif;
    font-weight: 400;
    fill: var(--text-soft);
  }
  .web-address {
    font-family: "Black Ops One", "Impact", sans-serif;
  }
  .web-domain { fill: var(--brand-blue); }
  .web-suffix { fill: var(--ink); }
  .brand-name {
    font-family: "Black Ops One", "Impact", sans-serif;
    fill: var(--brand-blue);
  }
</style>
</head>
<body>
<main class="canvas">
  <section class="sign" aria-label="Corvane Industrial Repair &amp; Tooling workshop sign">
    <svg viewBox="0 0 777 549" xmlns="http://www.w3.org/2000/svg">
      <defs>
        <linearGradient id="brushed-steel" x1="0" y1="0" x2="0" y2="1">
          <stop offset="0" stop-color="#5b5c5f"/>
          <stop offset="0.5" stop-color="#3c3d40"/>
          <stop offset="1" stop-color="#55565a"/>
        </linearGradient>
      </defs>

      <!-- Headline -->
      <g class="headline" fill="url(#brushed-steel)">
        <text x="46" y="143" font-size="96" textLength="681" lengthAdjust="spacingAndGlyphs">ENGINEERING</text>
        <text x="46" y="231" font-size="86" textLength="684" lengthAdjust="spacingAndGlyphs">&amp; FABRICATION</text>
      </g>

      <!-- Services band -->
      <rect class="band-rule" x="0" y="250" width="777" height="5" fill="var(--brand-blue)"/>
      <rect class="band-backdrop" x="0" y="255" width="777" height="186" fill="var(--band)" role="img" aria-label="Faint photo of workshop machinery and fabricated steel parts"/>
      <polygon class="band-tab" points="0,250 357,250 339,301 0,301" fill="var(--brand-blue)"/>
      <text class="tab-label" x="23" y="284" font-size="24" textLength="190" lengthAdjust="spacingAndGlyphs">SPECIALISTS IN</text>

      <g class="services">
        <text class="service" x="22" y="359" font-size="44" textLength="90" lengthAdjust="spacingAndGlyphs">DESIGN</text>
        <line class="service-divider" x1="126" y1="317" x2="126" y2="371"/>
        <text class="service" x="138" y="359" font-size="44" textLength="211" lengthAdjust="spacingAndGlyphs">MANUFACTURING</text>
        <line class="service-divider" x1="364" y1="317" x2="364" y2="371"/>
        <text class="service" x="376" y="359" font-size="44" textLength="173" lengthAdjust="spacingAndGlyphs">INSTALLATION</text>
        <line class="service-divider" x1="562" y1="317" x2="562" y2="371"/>
        <text class="service" x="575" y="359" font-size="44" textLength="175" lengthAdjust="spacingAndGlyphs">MAINTENANCE</text>
      </g>
      <text class="tagline" x="388" y="399" font-size="22" text-anchor="middle" textLength="546" lengthAdjust="spacingAndGlyphs">of industrial and commercial infrastructure.</text>

      <!-- Footer -->
      <text class="web-address" x="22" y="524" font-size="30" textLength="461" lengthAdjust="spacingAndGlyphs"><tspan class="web-domain">CORVANEREPAIR</tspan><tspan class="web-suffix">.NET.AU</tspan></text>
      <text class="brand-name" x="505" y="524" font-size="76" textLength="243" lengthAdjust="spacingAndGlyphs">CIRT</text>
    </svg>
  </section>
</main>
</body>
</html>
```